The Vixen Rides Again Line of Sparkling Wine & Spirits

Back info: Tara Rose Whitfield Owner 209-555-0143 1480 E. Harlow Rd, Bldg. 7, & 8, Lodi Ca. 95299
Sparkling Wines & Memorabilia www.thevixenridesagain.example
Ok I have uploaded the winning design. The color that I am after is the Fushia, Raspberry, Red, Matte Satin Matalic Finish. With a 24 Karet Gold color Foil. The Bottle is on the top row and it's the 2nd Bottle in. That is the Color that I want. This is the style of font. Make sure that you put what we're advertising. Good Luck to you all. Warmest regards, Tara
Target Market(s)
21 & up UniSex
Industry/Entity Type
Sparkling Wine and Memorabilia
Contact Information for Business Card
there listed up above.....

```html
<!DOCTYPE html>
<html lang="en">
<head>
<meta charset="utf-8">
<title>The Vixen Rides Again – Business Card</title>
<link rel="stylesheet" href="https://fonts.googleapis.com/css2?family=Arimo:wght@400;700&display=swap">
<style>
  :root {
    --page-bg: #e4e4e4;
    --card-white: #ffffff;
    --fuchsia: #c0136f;
    --fuchsia-bright: #e11a91;
    --fuchsia-deep: #951350;
    --gold: #e2a52c;
    --bronze-dark: #5e3312;
    --bronze-light: #b47a3c;
    --ink: #3b3b3b;
    --rule: #cfcfcf;
    --logo-ink: #3a3a3c;
  }
  * { box-sizing: border-box; margin: 0; padding: 0; }
  html, body {
    width: 1200px;
    height: 1200px;
    overflow: hidden;
    background: var(--page-bg);
    font-family: "Arimo", Arial, sans-serif;
  }
  .stage { position: relative; width: 1200px; height: 1200px; }
  .card {
    position: absolute;
    left: 256px;
    width: 688px;
    height: 393px;
    overflow: hidden;
  }

  /* Contact side */
  .card--contact { top: 159px; background: var(--card-white); }
  .faint-bottle {
    position: absolute;
    left: 92px; top: 0;
    width: 122px; height: 372px;
    border-radius: 30px 30px 10px 10px;
    background: linear-gradient(180deg, rgba(192,19,111,0.05), rgba(192,19,111,0.08));
  }
  .bottle-mini {
    position: absolute;
    left: 595px; top: 41px;
    width: 50px; height: 157px;
    border-radius: 12px 12px 5px 5px;
    background: linear-gradient(90deg, #a8105f, #e01a8e 50%, #a8105f);
  }
  .holder-name {
    position: absolute;
    left: 48px; top: 240px;
    font-size: 27px; font-weight: 700;
    color: var(--fuchsia);
    letter-spacing: 0.2px;
  }
  .holder-role {
    position: absolute;
    left: 48px; top: 268px;
    font-size: 17px;
    color: var(--gold);
  }
  .divider {
    position: absolute;
    left: 48px; top: 297px;
    width: 597px; height: 1px;
    background: var(--rule);
  }
  .phone {
    position: absolute;
    left: 48px; top: 309px;
    display: flex; align-items: center; gap: 9px;
    font-size: 16px; color: var(--ink);
  }
  .phone svg { width: 14px; height: 14px; fill: var(--fuchsia); }
  .address {
    position: absolute;
    right: 40px; top: 311px;
    font-size: 16px; color: var(--ink);
  }
  .footer-bands { position: absolute; left: 0; bottom: 0; width: 688px; height: 32px; }
  .web {
    position: absolute;
    right: 42px; bottom: 5px;
    font-size: 16px; color: #ffffff;
  }

  /* Brand side */
  .card--brand {
    top: 653px;
    background: radial-gradient(ellipse 65% 70% at 50% 42%, var(--fuchsia-bright) 0%, #c8157c 45%, var(--fuchsia-deep) 100%);
  }
  .bottle-hero {
    position: absolute;
    left: 102px; top: 65px;
    width: 74px; height: 257px;
    border-radius: 18px 18px 8px 8px;
    background: linear-gradient(90deg, #a30f5b, #e61c94 50%, #a30f5b);
  }
  .brand-name {
    position: absolute;
    left: 189px; top: 176px;
    width: 368px;
    text-align: center;
    font-size: 35px; font-weight: 700;
    color: var(--logo-ink);
    white-space: nowrap;
  }
  .brand-rule {
    position: absolute;
    left: 189px; top: 229px;
    width: 368px; height: 1px;
    background: rgba(90, 20, 60, 0.45);
  }
  .tagline {
    position: absolute;
    left: 189px; top: 238px;
    width: 368px;
    text-align: center;
    font-size: 17px;
    letter-spacing: 1.6px;
    color: #ffffff;
    white-space: nowrap;
  }
  .tagline strong { font-weight: 700; }
</style>
</head>
<body>
<main class="stage">

  <section class="card card--contact">
    <div class="faint-bottle" role="img" aria-label="Faint decorative wine bottle illustration"></div>
    <div class="bottle-mini" role="img" aria-label="Fuchsia sparkling wine bottle illustration"></div>

    <h1 class="holder-name">TARA ROSE WHITFIELD</h1>
    <p class="holder-role">Owner</p>
    <div class="divider"></div>

    <p class="phone">
      <svg viewBox="0 0 24 24" aria-hidden="true"><path d="M6.6 10.8a15.2 15.2 0 0 0 6.6 6.6l2.2-2.2c.3-.3.7-.4 1-.2 1.1.4 2.3.6 3.6.6.6 0 1 .4 1 1V20c0 .6-.4 1-1 1A17 17 0 0 1 3 4c0-.6.4-1 1-1h3.5c.6 0 1 .4 1 1 0 1.3.2 2.5.6 3.6.1.3 0 .7-.2 1z"/></svg>
      <span>209-555-0143 1480</span>
    </p>
    <p class="address">E. Harlow Rd, Bldg. 7, &amp; 8, Lodi Ca. 95299</p>

    <svg class="footer-bands" viewBox="0 0 688 32" aria-hidden="true">
      <defs>
        <linearGradient id="bronze" x1="0" x2="1">
          <stop offset="0" stop-color="#5e3312"/>
          <stop offset="0.45" stop-color="#b47a3c"/>
          <stop offset="1" stop-color="#5e3312"/>
        </linearGradient>
      </defs>
      <rect x="0" y="16" width="688" height="16" fill="#b0145f"/>
      <polygon points="0,0 398,0 388,16 0,16" fill="url(#bronze)"/>
      <polygon points="0,14 390,14 388,17 0,17" fill="#ffffff"/>
      <polygon points="404,0 688,0 688,32 384,32 396,16" fill="#b0145f"/>
    </svg>
    <p class="web">www.thevixenridesagain.example</p>
  </section>

  <section class="card card--brand">
    <div class="bottle-hero" role="img" aria-label="Fuchsia sparkling wine bottle illustration with gold neck"></div>
    <p class="brand-name">The Vixen Rides Again</p>
    <div class="brand-rule"></div>
    <p class="tagline">SPARKLING <strong>WINES &amp; MEMORABILIA</strong></p>
  </section>

</main>
</body>
</html>
```